A resume/portfolio website for myself

I'm an independent software contractor, architect, tech trainer. I need a web site to present myself. Many ready to use portfolio designs are too artistic and focused on presenting design skills of the person. I like a nice website but the content should be a little less graphic than if you would present a graphic designer. Content could be presentation of me, core skill qualities and services and resume. Potentially a page with my tech courses in the longer run

```html
<!DOCTYPE html>
<html lang="en">
<head>
<meta charset="utf-8">
<title>Daniel Varga — Software Contractor</title>
<link href="https://fonts.googleapis.com/css2?family=Montserrat:wght@500;600;700;800&family=Ubuntu:wght@400;500;700&family=Courier+Prime:wght@400;700&display=swap" rel="stylesheet">
<style>
:root{
  --ink:#1c2331;
  --heading:#2b2f36;
  --muted:#5f6670;
  --soft:#8a919a;
  --accent:#6b7b95;
  --band:#f3f3f4;
  --field:#f1f1f1;
  --line:#d7d9dc;
  --bar:#9ea4ac;
  --white:#fff;
}
*{box-sizing:border-box;margin:0;padding:0}
html,body{width:1200px;height:3688px;overflow:hidden;background:var(--white)}
body{font-family:'Ubuntu',sans-serif;color:var(--muted);position:relative}
.page{position:relative;width:1200px;height:3688px;overflow:hidden}
.abs{position:absolute}
.center{position:absolute;left:0;width:1200px;text-align:center}

/* nav */
.brand{left:12px;top:12px;font-family:'Montserrat',sans-serif;font-weight:800;font-size:30px;color:var(--ink);letter-spacing:-1px}
.nav{left:441px;top:18px;display:flex;gap:26px;font-size:10px;color:var(--soft)}
.nav .on{color:var(--ink)}
.btn{background:var(--ink);color:#fff;font-size:10px;display:flex;align-items:center;justify-content:center;box-shadow:0 4px 8px rgba(0,0,0,.25)}
.btn-resume{left:1062px;top:12px;width:120px;height:26px}

/* hero */
.hero-bg{left:0;top:0;width:1200px;height:590px}
.quote{font-family:'Courier Prime',monospace;font-size:19px;color:#555b63}
.name{font-family:'Montserrat',sans-serif;font-weight:800;font-size:44px;color:#3b3f46;letter-spacing:1px}
.roles{font-family:'Montserrat',sans-serif;font-weight:700;font-size:10.5px;letter-spacing:3px;color:var(--ink)}
.roles span{color:var(--soft);font-weight:500}
.avatar{left:550px;top:248px;width:100px;height:100px;border-radius:50%;background:radial-gradient(circle at 50% 40%,#8b6a58,#3b3c42 70%)}
.lede{left:420px;width:360px;text-align:center;font-size:9.5px;line-height:15.5px;color:#666c74}
.sig{left:560px;top:484px;width:80px;height:28px;background:linear-gradient(90deg,#e3e3e5,#d2d3d6);border-radius:3px}

/* headings */
.h2{font-family:'Montserrat',sans-serif;font-weight:800;font-size:26px;color:var(--heading)}
.h2 em{font-style:normal;color:#666a70}

/* timeline */
.tl-line{left:599px;top:730px;width:1px;height:500px;border-left:1px dashed #c9ccd0}
.tl-dot{width:50px;height:50px;border-radius:50%;background:var(--ink);border:3px solid #fff;box-shadow:0 0 0 1px #d5d7da;display:flex;align-items:center;justify-content:center}
.tl-dot span{width:16px;height:16px;border-radius:50%;background:#e8b52a}
.tl-role{width:220px}
.tl-role.left{left:327px;text-align:right}
.tl-role.right{left:652px}
.tl-role h4{font-family:'Montserrat',sans-serif;font-weight:700;font-size:11px;letter-spacing:3px;color:var(--ink)}
.tl-role b{display:block;font-size:10.5px;color:var(--ink);margin-top:3px}
.tl-role p{font-size:9.5px;color:var(--soft);margin-top:4px}
.tl-role i{display:block;font-style:normal;font-size:9.5px;color:var(--accent);margin-top:4px}
.tl-card{width:314px;height:126px;background:#fff;box-shadow:0 0 10px rgba(0,0,0,.1);padding:18px 16px;font-size:9.5px;line-height:15.7px;color:#777d85}
.tl-card.left{left:235px}
.tl-card.right{left:653px}
.tl-tick{width:12px;height:1px;background:var(--ink)}

/* bands */
.band{left:0;width:1200px}

/* education */
.edu-card{top:1548px;width:295px;height:110px;background:#fff;box-shadow:0 0 10px rgba(0,0,0,.08);text-align:center;padding-top:42px}
.edu-card h5{font-size:11px;color:var(--ink);font-weight:700}
.edu-card p{font-size:9.5px;color:var(--soft);margin-top:6px}
.edu-card i{display:block;font-style:normal;font-size:9px;color:var(--accent);margin-top:6px}
.badge{width:50px;height:50px;border-radius:50%;background:var(--ink);display:flex;align-items:center;justify-content:center}
.badge span{width:18px;height:18px;border-radius:3px;background:#e2662b}

/* skills */
.ring{top:1890px;width:188px;text-align:center}
.ring svg{display:block;margin:0 auto}
.ring .pct{position:absolute;left:0;width:188px;top:34px;font-family:'Montserrat',sans-serif;font-weight:700;font-size:19px;color:var(--ink)}
.ring .pct small{font-size:11px}
.ring h6{margin-top:14px;font-family:'Montserrat',sans-serif;font-weight:700;font-size:13px;letter-spacing:3px;color:var(--ink)}
.ring h6 small{font-family:'Ubuntu',sans-serif;letter-spacing:0;font-size:10px;font-weight:500}
.ring .lvl{font-size:9px;color:var(--soft);margin-top:3px}
.ring p{font-size:9.5px;line-height:15.5px;color:#787e86;margin-top:3px}
.chip{width:168px;height:50px;background:#fff;box-shadow:0 0 8px rgba(0,0,0,.1);text-align:center;padding-top:7px}
.chip .track{margin:0 auto;width:156px;height:11px;background:#eceef0;position:relative}
.chip .fill{position:absolute;left:0;top:0;height:11px;width:90%;background:var(--bar);font-size:7px;color:#fff;text-align:center;line-height:11px}
.chip b{display:block;margin-top:12px;font-size:10.5px;color:var(--ink)}

/* portfolio */
.work{width:169px;height:169px;background:#fff;box-shadow:0 0 8px rgba(0,0,0,.1);text-align:center;padding:6px}
.work .shot{height:100px;width:157px}
.work h5{margin-top:12px;font-size:11px;color:var(--ink);font-weight:700}
.work p{font-size:9px;color:var(--soft);margin-top:3px}
.work i{display:block;font-style:normal;font-size:9px;color:var(--accent);margin-top:4px;font-weight:500}

/* contact */
.field{background:var(--field);font-size:9.5px;color:#8d939a;display:flex;align-items:center;justify-content:center}
.info{top:3349px;width:169px;height:112px;background:#fff;box-shadow:0 0 10px rgba(0,0,0,.1);text-align:center;padding-top:62px}
.info b{font-size:11px;color:var(--ink);display:block}
.info p{font-size:9.5px;color:var(--soft);margin-top:3px}
.ico{width:50px;height:50px;border-radius:50%;background:var(--ink);display:flex;align-items:center;justify-content:center}

/* footer */
.footer{left:0;top:3515px;width:1200px;height:173px;background:var(--band)}
.social{left:503px;top:3560px;display:flex;gap:12px;align-items:center}
.social span{width:20px;height:20px;border-radius:50%;background:var(--ink)}
.social strong{font-family:'Montserrat',sans-serif;font-weight:800;font-size:22px;color:var(--ink);margin:0 6px}
</style>
</head>
<body>
<div class="page">

  <!-- hero -->
  <svg class="abs hero-bg" viewBox="0 0 1200 590" role="img" aria-label="Soft grey workspace backdrop behind the introduction">
    <defs>
      <linearGradient id="heroShade" x1="0" y1="0" x2="1" y2="0">
        <stop offset="0" stop-color="#ffffff"/>
        <stop offset=".35" stop-color="#f1f1f2"/>
        <stop offset="1" stop-color="#dcdde0"/>
      </linearGradient>
    </defs>
    <polygon points="0,0 1200,0 1200,515 0,587" fill="url(#heroShade)"/>
  </svg>

  <div class="abs brand">DV</div>
  <nav class="abs nav"><span class="on">About Me</span><span>Experience</span><span>Education</span><span>Skills</span><span>Work</span><span>Contact</span></nav>
  <div class="abs btn btn-resume">Download My Resume</div>

  <div class="center quote" style="top:103px">("Hello World! I am..")</div>
  <div class="center name" style="top:140px">DANIEL VARGA</div>
  <div class="center roles" style="top:214px"><span>( </span>SOFTWARE CONTRACTOR <span>/</span> ARCHITECT <span>/</span> TECH TRAINER <span> )</span></div>
  <div class="abs avatar" role="img" aria-label="Portrait photo of Daniel Varga"></div>
  <p class="abs lede" style="top:362px">Lorem ipsum dolor sit amet, consectetur adipiscing elit, sed do eiusmod tempor incididunt ut labore et dolore magna aliqua. Quis ipsum suspendisse ultrices grav ida eleifend. Risus commodo viverra maecenas accumsan lacus vel facilisis. Vivamus elementum semper nisi. Aenean vulputate eleifend ligula pede tellus.</p>
  <p class="abs lede" style="top:434px">Aenean leo, porttitor eu, consequat vitae, eleifend ac, enim. Aliquam lorem ante, dapibus in, viverra quis, feugiat a, tellus. Donec justo, fringilla vel, aliquet nec.</p>
  <div class="abs sig" role="img" aria-label="Handwritten signature"></div>

  <!-- experience -->
  <div class="center quote" style="top:604px">("I have worked at..")</div>
  <div class="center h2" style="top:646px"><em>WORK</em> EXPERIENCE</div>
  <div class="abs tl-line"></div>

  <div class="abs tl-role left" style="top:725px"><h4>LEAD R&amp;D ENGINEER</h4><b>Corvent</b><p>Jul 2017 – Present</p><i>Millbrook, NC 27000</i></div>
  <div class="abs tl-tick" style="left:558px;top:733px"></div>
  <div class="abs tl-dot" style="left:575px;top:708px"><span></span></div>
  <div class="abs tl-card right" style="top:707px">Lorem ipsum dolor sit amet, consectetur adipiscing elit, sed do eiusmod tempor incididunt ut labore et dolore magna aliqua. Quis ipsum suspendisse ultrices grav ida eleifend. Risus commodo viverra maecenas accumsan lacus vel facilisis. Vivamus elementum semper nisi. Aenean vulputate eleifend ligula pede tellus. Aenean leo, porttitor eu, consequat vitae, eleifend ac, enim.</div>

  <div class="abs tl-card left" style="top:869px">Lorem ipsum dolor sit amet, consectetur adipiscing elit, sed do eiusmod tempor incididunt ut labore et dolore magna aliqua. Quis ipsum suspendisse ultrices grav ida eleifend. Risus commodo viverra maecenas accumsan lacus vel facilisis. Vivamus elementum semper nisi. Aenean vulputate eleifend ligula pede tellus. Aenean leo, porttitor eu, consequat vitae, eleifend ac, enim.</div>
  <div class="abs tl-dot" style="left:575px;top:870px"><span style="background:#c8322f"></span></div>
  <div class="abs tl-tick" style="left:630px;top:895px"></div>
  <div class="abs tl-role right" style="top:888px"><h4>LEAD R&amp;D ENGINEER</h4><b>Corvent</b><p>Jul 2017 – Present</p><i>Millbrook, NC 27000</i></div>

  <div class="abs tl-role left" style="top:1050px"><h4>LEAD R&amp;D ENGINEER</h4><b>Corvent</b><p>Jul 2017 – Present</p><i>Millbrook, NC 27000</i></div>
  <div class="abs tl-tick" style="left:558px;top:1058px"></div>
  <div class="abs tl-dot" style="left:575px;top:1033px"><span style="background:#2f74b5"></span></div>
  <div class="abs tl-card right" style="top:1032px">Lorem ipsum dolor sit amet, consectetur adipiscing elit, sed do eiusmod tempor incididunt ut labore et dolore magna aliqua. Quis ipsum suspendisse ultrices grav ida eleifend. Risus commodo viverra maecenas accumsan lacus vel facilisis. Vivamus elementum semper nisi. Aenean vulputate eleifend ligula pede tellus. Aenean leo, porttitor eu, consequat vitae, eleifend ac, enim.</div>

  <div class="abs tl-card left" style="top:1194px">Lorem ipsum dolor sit amet, consectetur adipiscing elit, sed do eiusmod tempor incididunt ut labore et dolore magna aliqua. Quis ipsum suspendisse ultrices grav ida eleifend. Risus commodo viverra maecenas accumsan lacus vel facilisis. Vivamus elementum semper nisi. Aenean vulputate eleifend ligula pede tellus. Aenean leo, porttitor eu, consequat vitae, eleifend ac, enim.</div>
  <div class="abs tl-dot" style="left:575px;top:1195px"><span style="background:#fff"></span></div>
  <div class="abs tl-tick" style="left:630px;top:1220px"></div>
  <div class="abs tl-role right" style="top:1213px"><h4>LEAD R&amp;D ENGINEER</h4><b>Corvent</b><p>Jul 2017 – Present</p><i>Millbrook, NC 27000</i></div>

  <!-- education band -->
  <svg class="abs band" style="top:1339px" width="1200" height="425" viewBox="0 0 1200 425"><polygon points="0,61 1200,0 1200,362 0,422" fill="#f3f3f4"/></svg>
  <div class="center quote" style="top:1416px">("I studied at..")</div>
  <div class="center h2" style="top:1459px"><em>MY</em> EDUCATION</div>
  <div class="abs edu-card" style="left:296px"><h5>Northfield State University</h5><p>Master of Science (M.S.) - Computer Science</p><i>1990 - 1992</i></div>
  <div class="abs edu-card" style="left:610px"><h5>Northfield State University</h5><p>Bachelor of Science (B.S.) - Mathematics &amp; Computer Science</p><i>1983 - 1987</i></div>
  <div class="abs badge" style="left:418px;top:1523px"><span></span></div>
  <div class="abs badge" style="left:732px;top:1523px"><span></span></div>

  <!-- skills -->
  <div class="center quote" style="top:1778px">("What I have acquired..")</div>
  <div class="center h2" style="top:1821px"><em>MY</em> SKILLS <em>&amp;</em> SPECIALITIES</div>

  <div class="abs ring" style="left:225px">
    <svg width="96" height="96" viewBox="0 0 96 96"><circle cx="48" cy="48" r="43" fill="none" stroke="#eceef0" stroke-width="5"/><circle cx="48" cy="48" r="43" fill="none" stroke="#98a0aa" stroke-width="5" stroke-dasharray="243 270" transform="rotate(-90 48 48)"/></svg>
    <div class="pct">90<small>%</small></div>
    <h6>C<small> , 4 Years</small></h6><div class="lvl">Expert</div>
    <p>Lorem ipsum dolor sit amet, consect etur adipiscing elit, sed do eiusmod.</p>
  </div>
  <div class="abs ring" style="left:413px">
    <svg width="96" height="96" viewBox="0 0 96 96"><circle cx="48" cy="48" r="43" fill="none" stroke="#eceef0" stroke-width="5"/><circle cx="48" cy="48" r="43" fill="none" stroke="#98a0aa" stroke-width="5" stroke-dasharray="243 270" transform="rotate(-90 48 48)"/></svg>
    <div class="pct">90<small>%</small></div>
    <h6>C++<small> , 4 Years</small></h6><div class="lvl">Expert</div>
    <p>Lorem ipsum dolor sit amet, consect etur adipiscing elit, sed do eiusmod.</p>
  </div>
  <div class="abs ring" style="left:599px">
    <svg width="96" height="96" viewBox="0 0 96 96"><circle cx="48" cy="48" r="43" fill="none" stroke="#eceef0" stroke-width="5"/><circle cx="48" cy="48" r="43" fill="none" stroke="#98a0aa" stroke-width="5" stroke-dasharray="243 270" transform="rotate(-90 48 48)"/></svg>
    <div class="pct">90<small>%</small></div>
    <h6>PYTHON<small> , 4 Years</small></h6><div class="lvl">Expert</div>
    <p>Lorem ipsum dolor sit amet, consect etur adipiscing elit, sed do eiusmod.</p>
  </div>
  <div class="abs ring" style="left:787px">
    <svg width="96" height="96" viewBox="0 0 96 96"><circle cx="48" cy="48" r="43" fill="none" stroke="#eceef0" stroke-width="5"/><circle cx="48" cy="48" r="43" fill="none" stroke="#98a0aa" stroke-width="5" stroke-dasharray="243 270" transform="rotate(-90 48 48)"/></svg>
    <div class="pct">90<small>%</small></div>
    <h6>QT<small> , 4 Years</small></h6><div class="lvl">Expert</div>
    <p>Lorem ipsum dolor sit amet, consect etur adipiscing elit, sed do eiusmod.</p>
  </div>

  <div class="center quote" style="top:2104px">("Other Skills")</div>
  <div class="abs chip" style="left:235px;top:2151px"><div class="track"><div class="fill">90%</div></div><b>Network Communication</b></div>
  <div class="abs chip" style="left:422px;top:2151px"><div class="track"><div class="fill">90%</div></div><b>Debugging</b></div>
  <div class="abs chip" style="left:610px;top:2151px"><div class="track"><div class="fill">90%</div></div><b>Software Design &amp; Dev</b></div>
  <div class="abs chip" style="left:798px;top:2151px"><div class="track"><div class="fill">90%</div></div><b>GUI Framework Dev</b></div>
  <div class="abs chip" style="left:328px;top:2220px"><div class="track"><div class="fill">90%</div></div><b>Scientific Visualization</b></div>
  <div class="abs chip" style="left:516px;top:2220px"><div class="track"><div class="fill">90%</div></div><b>Message Passing Interface</b></div>
  <div class="abs chip" style="left:703px;top:2220px"><div class="track"><div class="fill">90%</div></div><b>Licensing Systems</b></div>

  <!-- portfolio band -->
  <svg class="abs band" style="top:2301px" width="1200" height="674" viewBox="0 0 1200 674"><polygon points="0,62 1200,0 1200,674 0,674" fill="#f3f3f4"/></svg>
  <div class="center quote" style="top:2380px">("Portfolio")</div>
  <div class="center h2" style="top:2421px"><em>MY</em> WORK</div>

  <div class="abs work" style="left:235px;top:2486px"><div class="shot" role="img" aria-label="Project screenshot: laptop with code" style="background:linear-gradient(135deg,#2c3645,#5a6b82)"></div><h5>Project Title</h5><p>C++, Python, QT</p><i>Learn More</i></div>
  <div class="abs work" style="left:422px;top:2486px"><div class="shot" role="img" aria-label="Project screenshot: web page layouts" style="background:linear-gradient(135deg,#e6e7ea,#3a4250)"></div><h5>Project Title</h5><p>C++, Python, QT</p><i>Learn More</i></div>
  <div class="abs work" style="left:610px;top:2486px"><div class="shot" role="img" aria-label="Project screenshot: developer at laptop" style="background:linear-gradient(135deg,#8b7760,#263040)"></div><h5>Project Title</h5><p>C++, Python, QT</p><i>Learn More</i></div>
  <div class="abs work" style="left:798px;top:2486px"><div class="shot" role="img" aria-label="Project screenshot: mobile app mockup" style="background:linear-gradient(135deg,#d9d4cf,#e0503e)"></div><h5>Project Title</h5><p>C++, Python, QT</p><i>Learn More</i></div>
  <div class="abs work" style="left:235px;top:2674px"><div class="shot" role="img" aria-label="Project screenshot: phone app mockup" style="background:linear-gradient(135deg,#6b5a4a,#1f3c4a)"></div><h5>Project Title</h5><p>C++, Python, QT</p><i>Learn More</i></div>
  <div class="abs work" style="left:422px;top:2674px"><div class="shot" role="img" aria-label="Project screenshot: monitor with code" style="background:linear-gradient(135deg,#3b4250,#13161c)"></div><h5>Project Title</h5><p>C++, Python, QT</p><i>Learn More</i></div>
  <div class="abs work" style="left:610px;top:2674px"><div class="shot" role="img" aria-label="Project screenshot: food website design" style="background:linear-gradient(135deg,#e8a23a,#2a2a2e)"></div><h5>Project Title</h5><p>C++, Python, QT</p><i>Learn More</i></div>
  <div class="abs work" style="left:798px;top:2674px"><div class="shot" role="img" aria-label="Project screenshot: laptop with code" style="background:linear-gradient(135deg,#232a36,#5d7290)"></div><h5>Project Title</h5><p>C++, Python, QT</p><i>Learn More</i></div>
  <div class="abs btn" style="left:544px;top:2862px;width:112px;height:32px">Load More</div>

  <!-- contact -->
  <div class="center quote" style="top:2991px">("Reach Out")</div>
  <div class="center h2" style="top:3034px">CONTACT <span style="color:var(--ink)">ME</span></div>
  <div class="abs field" style="left:235px;top:3100px;width:230px;height:30px">Your Ful Name</div>
  <div class="abs field" style="left:485px;top:3100px;width:231px;height:30px">Your Email Address</div>
  <div class="abs field" style="left:735px;top:3100px;width:232px;height:30px">Your Contact Number</div>
  <div class="abs field" style="left:235px;top:3149px;width:732px;height:106px;align-items:flex-start;padding-top:12px">Your Message</div>
  <div class="abs btn" style="left:544px;top:3275px;width:112px;height:32px">Send Message</div>

  <div class="abs info" style="left:328px"><b>Call Me</b><p>123 456 7890</p></div>
  <div class="abs info" style="left:516px"><b>Visit Me</b><p>Address Line 1, City 1234</p></div>
  <div class="abs info" style="left:703px"><b>Email Me</b><p>Contact@DanielVarga.com</p></div>
  <div class="abs ico" style="left:387px;top:3360px"><svg width="20" height="20" viewBox="0 0 24 24"><path d="M6.6 10.8a15.1 15.1 0 006.6 6.6l2.2-2.2a1 1 0 011-.25 11.4 11.4 0 003.6.57 1 1 0 011 1V20a1 1 0 01-1 1A17 17 0 013 4a1 1 0 011-1h3.5a1 1 0 011 1c0 1.25.2 2.45.57 3.57a1 1 0 01-.25 1z" fill="#fff"/></svg></div>
  <div class="abs ico" style="left:575px;top:3360px"><svg width="20" height="20" viewBox="0 0 24 24"><path d="M12 2a7 7 0 00-7 7c0 5.2 7 13 7 13s7-7.8 7-13a7 7 0 00-7-7zm0 9.5A2.5 2.5 0 1112 6.5a2.5 2.5 0 010 5z" fill="#fff"/></svg></div>
  <div class="abs ico" style="left:762px;top:3360px"><svg width="20" height="20" viewBox="0 0 24 24"><path d="M3 5h18v14H3z" fill="#fff"/><path d="M3 5l9 7 9-7" fill="none" stroke="#1c2331" stroke-width="2"/></svg></div>

  <!-- footer -->
  <div class="abs footer"></div>
  <div class="abs social"><span></span><span></span><strong>DV</strong><span></span><span></span></div>
  <div class="center" style="top:3593px;font-family:'Montserrat',sans-serif;font-weight:700;font-size:14px;letter-spacing:1px;color:#3b3f46">DANIEL VARGA</div>
  <div class="center" style="top:3628px;font-size:8.5px;color:var(--soft)">Copyright © 2020 Daniel Varga</div>
  <div class="center" style="top:3644px;font-size:9px;color:var(--accent)">Privacy / Terms</div>

</div>
</body>
</html>
```